Meadowlark Bloom Yard Website

I am looking for a website that allows me to be able to work on and make changes. I am looking to upload pictures to showcase my flowers, activities, and venue option at my garden. I am NOT tech savvy at all. I am looking to build my brand, and have options for click and purchase flowers or activities and or pay with swipe. I want to add my instagram and facebook pages and link those pages to each other. Also I would like to have a way to get their info for email updates on my new business. I want to advertise that my site is new and we are working at planting our Spring Flowers ;)

I want to be able to work on my website myself with ease. I want my products page to be easy to access - user friendly.

Target Market(s)

Local Florist, Grocers, growers, event venues, local flower farmers

Industry/Entity Type

Hospitality

Coding

Coded - Design and coding required

Number of Pages Required

5+ page

Font styles to use
Decorative

Requirements
Must have
• Must have radio buttons for my clients to sign up for contact page, be able to call and email me, find my facebook and instagram icon, select events, classes, merchandise and flower arrangements and pay with apple pay, venmo and square
Nice to have
• I am very much looking for something very similar to this website. Please refer to https://www.brindlewoodstems.com for what I desir. I have uploaded photographs, and my logo. I will also like on my homepage where all my flowers are to be able to write a brief introduction/brand
Should not have
• Any hidden secrets on how to add photos, change out photos or be difficult to manage

```html
<!DOCTYPE html>
<html lang="en">
<head>
<meta charset="utf-8">
<title>Meadowlark Bloom Yard</title>
<link href="https://fonts.googleapis.com/css2?family=Playfair+Display:wght@400;700&family=Lato:wght@400;700&family=Great+Vibes&display=swap" rel="stylesheet">
<style>
:root{
  --ink:#222;
  --muted:#8a8a8a;
  --line:#e6e6e6;
  --accent:#e6436b;
  --cta:#f15a3b;
  --paper:#fff;
  --soft:#f3f3f3;
  --cream:#fbf6ee;
  --serif:'Playfair Display', Georgia, serif;
  --sans:'Lato', Helvetica, Arial, sans-serif;
  --script:'Great Vibes', cursive;
}
*{box-sizing:border-box;margin:0;padding:0}
html,body{width:1200px;height:3508px;overflow:hidden;background:var(--paper);color:var(--ink);font-family:var(--sans)}
.page{position:relative;width:1200px;height:3508px}
section,header,footer{position:absolute;left:0;width:1200px}
.wrap{position:absolute;left:192px;width:816px}

/* header */
.site-header{top:0;height:112px;border-bottom:1px solid var(--line)}
.brand{position:absolute;left:192px;top:36px;font-family:var(--serif);font-size:24px;color:var(--accent);font-weight:400;white-space:nowrap}
.nav{position:absolute;left:486px;top:46px;display:flex;gap:24px;font-size:10px;letter-spacing:1.3px;font-weight:700;color:#555;white-space:nowrap}
.nav .active{color:var(--ink);border-bottom:2px solid var(--ink);padding-bottom:4px}
.tools{position:absolute;right:192px;top:43px;display:flex;gap:14px;align-items:center;font-size:10px;letter-spacing:1px;font-weight:700;white-space:nowrap}

/* hero */
.hero{top:112px;height:348px;background:var(--soft)}
.hero h1{position:absolute;left:192px;top:40px;font-family:var(--serif);font-size:46px;line-height:1.15;font-weight:700;width:420px}
.hero h1 em{font-style:normal;color:var(--accent)}
.hero p{position:absolute;left:192px;top:166px;width:340px;font-size:12px;line-height:1.7;color:var(--muted)}
.read-more{position:absolute;left:192px;top:226px;font-family:var(--script);font-size:30px;color:var(--accent)}
.hero-photo{position:absolute;left:600px;top:0;width:520px;height:348px;background:linear-gradient(120deg,#f3f3f3 0%,#e9b8cd 45%,#c73f7d 60%,#6c9a4d 80%,#f3f3f3 100%)}
.side-arrow{position:absolute;top:150px;font-size:18px;color:#aaa}

/* shop */
.filters{top:496px;height:30px}
.filters ul{list-style:none;display:flex;gap:24px;font-size:10px;letter-spacing:1.4px;color:var(--muted);font-weight:700}
.filters ul li:first-child{color:var(--ink)}
.filters .filter-btn{position:absolute;right:0;top:0;font-size:10px;letter-spacing:1.4px;font-weight:700}
.products{top:532px;height:580px}
.grid{display:grid;grid-template-columns:repeat(4,180px);column-gap:32px;row-gap:40px}
.product .photo{height:208px;position:relative}
.product .tag{position:absolute;left:10px;top:10px;background:var(--ink);color:#fff;font-size:9px;letter-spacing:1px;padding:3px 7px}
.product h3{font-size:10px;letter-spacing:1.2px;text-align:center;margin-top:14px;font-weight:700}
.product .price{font-size:11px;text-align:center;color:var(--muted);margin-top:4px}
.product .price s{margin-right:6px}

/* valentine */
.valentine{top:1200px;height:340px;background:var(--soft)}
.video{position:absolute;left:192px;top:60px;width:408px;height:268px;background:linear-gradient(135deg,#9bb7a8,#5e6f63 55%,#c9b29c)}
.play{position:absolute;left:174px;top:104px;width:60px;height:60px;border-radius:50%;background:#fff}
.valentine h2{position:absolute;left:640px;top:76px;font-family:var(--serif);font-size:28px;line-height:1.3;font-weight:400}
.valentine h2 em{font-style:normal;color:var(--accent)}
.valentine p{position:absolute;left:640px;top:170px;width:340px;font-size:12px;line-height:1.7;color:var(--muted)}
.perks{position:absolute;left:640px;top:232px;list-style:none;font-size:12px;color:#555}
.perks li{display:flex;align-items:center;gap:12px;margin-bottom:12px}

/* experts */
.experts{top:1660px;height:400px;text-align:center}
.section-title{font-family:var(--serif);font-size:30px;font-weight:400}
.section-lede{width:440px;margin:14px auto 0;font-size:12px;line-height:1.7;color:var(--muted)}
.team{position:absolute;left:192px;top:152px;width:816px;display:grid;grid-template-columns:repeat(4,1fr)}
.member .avatar{width:140px;height:140px;border-radius:50%;margin:0 auto}
.member h4{font-size:10px;letter-spacing:1.3px;margin-top:18px}
.member span{font-size:10px;color:var(--muted)}

/* newsletter */
.newsletter{top:2088px;height:332px;background:linear-gradient(100deg,#3c3a2f,#7c8a63 35%,#5a4c44 60%,#2f3b2a)}
.newsletter h2{position:absolute;left:0;width:1200px;text-align:center;top:120px;font-family:var(--serif);font-size:24px;color:#fff;font-weight:400}
.signup{position:absolute;left:400px;top:170px;display:flex}
.signup .field{width:292px;height:40px;background:#fff;font-size:11px;color:var(--muted);padding:13px 16px}
.signup .btn{width:108px;height:40px;background:var(--cta);color:#fff;font-size:10px;letter-spacing:1.4px;font-weight:700;text-align:center;line-height:40px}

/* blog */
.blog{top:2480px;height:440px;text-align:center}
.posts{position:absolute;left:192px;top:128px;width:816px;display:grid;grid-template-columns:repeat(3,260px);column-gap:18px;text-align:center}
.post .thumb{height:172px;position:relative}
.post .label{position:absolute;left:10px;top:10px;background:#fff;font-size:8px;letter-spacing:1px;padding:3px 6px;font-weight:700}
.post h3{font-family:var(--serif);font-size:18px;font-weight:400;margin-top:22px}
.post p{font-size:11px;line-height:1.6;color:var(--muted);width:220px;margin:8px auto 0}

/* testimonial */
.testimonial{top:2940px;height:240px;text-align:center}
.testimonial .avatar{width:52px;height:52px;border-radius:50%;margin:40px auto 0;background:linear-gradient(135deg,#f0a33a,#c83c3c)}
.testimonial blockquote{font-family:var(--serif);font-size:20px;line-height:1.5;width:500px;margin:18px auto 0}
.testimonial cite{display:block;font-style:normal;font-size:9px;letter-spacing:1.3px;font-weight:700;margin-top:18px}
.testimonial cite span{display:block;color:var(--muted);font-weight:400;margin-top:3px}
.testimonial .side-arrow{top:112px}

/* footer */
.site-footer{top:3248px;height:260px;background:var(--cream)}
.cols{position:absolute;left:192px;top:44px;width:816px;display:grid;grid-template-columns:repeat(4,1fr)}
.cols h5{font-size:9px;letter-spacing:1.4px;margin-bottom:12px}
.cols ul{list-style:none;font-size:10px;line-height:2;color:var(--muted)}
.payments{position:absolute;left:0;width:1200px;top:184px;display:flex;justify-content:center;gap:8px}
.payments span{width:30px;height:18px;border-radius:3px;background:#c9c3b8}
.payments span:nth-child(2){background:#2f2f2f}
</style>
</head>
<body>
<div class="page">

<header class="site-header">
  <div class="brand">Meadowlark Bloom Yard</div>
  <nav class="nav"><span class="active">HOME</span><span>PAGES</span><span>SHOP</span><span>PORTFOLIO</span><span>BLOG</span><span>ELEMENTS</span></nav>
  <div class="tools">
    <svg width="13" height="13" viewBox="0 0 13 13" fill="none" stroke="#222" stroke-width="1.5"><circle cx="5.5" cy="5.5" r="4.2"/><path d="M8.6 8.6 12 12"/></svg>
    <svg width="13" height="13" viewBox="0 0 13 13" fill="none" stroke="#222" stroke-width="1.3"><path d="M2 4h9l-1 8H3z"/><path d="M4.5 4a2 2 0 0 1 4 0"/></svg>
    <span>CART (0)</span>
  </div>
</header>

<section class="hero">
  <span class="side-arrow" style="left:14px">‹</span><span class="side-arrow" style="right:14px">›</span>
  <h1>Send <em>flowers</em> like you mean it.</h1>
  <p>Fresh stems cut each morning from our own beds, wrapped by hand and delivered to your door with care and a note.</p>
  <div class="read-more">Read More</div>
  <div class="hero-photo" role="img" aria-label="Two pink tulips with green leaves on a pale background"></div>
</section>

<section class="filters">
  <div class="wrap">
    <ul><li>ALL</li><li>CACTUSES</li><li>EXOTIC</li><li>GARDEN</li><li>PARTY</li><li>TROPICAL</li><li>WEDDING</li></ul>
    <div class="filter-btn">FILTER ▾</div>
  </div>
</section>

<section class="products">
  <div class="wrap grid">
    <div class="product"><div class="photo" role="img" aria-label="Small cactus in a brass pot" style="background:linear-gradient(#f1f1ef,#b89a5a)"></div><h3>DESERT GLOW</h3><div class="price">$35.00</div></div>
    <div class="product"><div class="photo" role="img" aria-label="Pink star lily stems" style="background:linear-gradient(135deg,#f4f4f4,#e07fa0,#f4f4f4)"></div><h3>STARLIGHT LILIES</h3><div class="price">$42.00</div></div>
    <div class="product"><div class="photo" role="img" aria-label="Snake plant in a white pot" style="background:linear-gradient(#f4f4f4,#4f6e45,#e9e9e9)"></div><h3>SNAKE PLANT</h3><div class="price">$28.00</div></div>
    <div class="product"><div class="photo" role="img" aria-label="Single pink tulip" style="background:linear-gradient(#f4f4f4,#d0508a,#5f9448)"></div><h3>PINK TULIP STEM</h3><div class="price">$12.00</div></div>
    <div class="product"><div class="photo" role="img" aria-label="Orange rose bouquet" style="background:linear-gradient(135deg,#f4f4f4,#e97a3c,#f4f4f4)"><span class="tag">SALE</span></div><h3>SUNSET ROSES</h3><div class="price"><s>$60.00</s>$48.00</div></div>
    <div class="product"><div class="photo" role="img" aria-label="Aloe plant in a white pot" style="background:linear-gradient(#f4f4f4,#7fa37a,#ececec)"></div><h3>ALOE GREEN</h3><div class="price">$22.00</div></div>
    <div class="product"><div class="photo" role="img" aria-label="Hanging trailing plant in a basket" style="background:linear-gradient(#f4f4f4,#3f6b38,#f4f4f4)"></div><h3>HANGING IVY</h3><div class="price">$30.00</div></div>
    <div class="product"><div class="photo" role="img" aria-label="Red exotic bloom with leaves" style="background:linear-gradient(135deg,#f4f4f4,#c62a3b,#4e7a3d)"></div><h3>RED PASSION</h3><div class="price">$38.00</div></div>
  </div>
</section>

<section class="valentine">
  <div class="video" role="img" aria-label="Video still of two gardeners in hats outdoors">
    <div class="play"><svg width="60" height="60" viewBox="0 0 60 60"><path d="M25 21l14 9-14 9z" fill="#222"/></svg></div>
  </div>
  <h2>Suprise Your <em>Valentine!</em><br>Let us arrange a smile.</h2>
  <p>Choose a bouquet, add a message and we will pick, wrap and deliver it fresh on the day you choose.</p>
  <ul class="perks">
    <li><svg width="12" height="11" viewBox="0 0 12 11"><path d="M6 10.5 1 5.5A2.8 2.8 0 0 1 6 2a2.8 2.8 0 0 1 5 3.5z" fill="#e6436b"/></svg>Hand picked just for you</li>
    <li><svg width="12" height="11" viewBox="0 0 12 11"><path d="M6 10.5 1 5.5A2.8 2.8 0 0 1 6 2a2.8 2.8 0 0 1 5 3.5z" fill="#e6436b"/></svg>Unique flower arrangements</li>
    <li><svg width="12" height="11" viewBox="0 0 12 11"><path d="M6 10.5 1 5.5A2.8 2.8 0 0 1 6 2a2.8 2.8 0 0 1 5 3.5z" fill="#e6436b"/></svg>Best way to say you care</li>
  </ul>
</section>

<section class="experts">
  <h2 class="section-title">Flower Experts</h2>
  <p class="section-lede">A small team of growers and florists who plan, plant and arrange every stem, from seed to finished bouquet.</p>
  <div class="team">
    <div class="member"><div class="avatar" role="img" aria-label="Portrait of a florist" style="background:#6b5a48"></div><h4>HAZEL MORROW</h4><span>Head Grower</span></div>
    <div class="member"><div class="avatar" role="img" aria-label="Portrait of a florist" style="background:#c47a4e"></div><h4>IVY CALLOWAY</h4><span>Florist</span></div>
    <div class="member"><div class="avatar" role="img" aria-label="Portrait of a florist" style="background:#a89a83"></div><h4>JUNE PARRISH</h4><span>Designer</span></div>
    <div class="member"><div class="avatar" role="img" aria-label="Portrait of a florist wearing a flower crown" style="background:#e3a23b"></div><h4>ROSA DELANEY</h4><span>Events</span></div>
  </div>
</section>

<section class="newsletter" role="img" aria-label="Friends laughing together in a leafy greenhouse">
  <h2>Join The Colorful Bunch</h2>
  <div class="signup"><div class="field">Your email</div><div class="btn">SUBSCRIBE</div></div>
</section>

<section class="blog">
  <h2 class="section-title">From our Blog</h2>
  <p class="section-lede">Growing notes, arranging tips and news from the beds as we plant our spring flowers.</p>
  <div class="posts">
    <div class="post"><div class="thumb" role="img" aria-label="Hands wrapping a bouquet" style="background:linear-gradient(135deg,#b9926f,#e0b6a4)"><span class="label">FLOWERS</span></div><h3>Flower Power</h3><p>Simple ways to keep cut stems fresh for a full week at home.</p></div>
    <div class="post"><div class="thumb" role="img" aria-label="Florist arranging flowers at a table" style="background:linear-gradient(135deg,#e9e4e1,#c78a95)"><span class="label">LOCAL</span></div><h3>Local Florists</h3><p>Meet the growers and shops we partner with across the valley.</p></div>
    <div class="post"><div class="thumb" role="img" aria-label="White tulips in a vase" style="background:linear-gradient(135deg,#f1efe9,#b7c3a2)"><span class="label">SEASON</span></div><h3>Flower Beauty</h3><p>Our favourite white blooms for spring weddings and parties.</p></div>
  </div>
</section>

<section class="testimonial">
  <span class="side-arrow" style="left:320px">‹</span><span class="side-arrow" style="right:320px">›</span>
  <div class="avatar" role="img" aria-label="Customer photo"></div>
  <blockquote>Lorem ipsum dolor sit amet, consectetur adipiscing elit donec commodo ligula eget.</blockquote>
  <cite>MARGOT ELLIS<span>Customer</span></cite>
</section>

<footer class="site-footer">
  <div class="cols">
    <div><h5>CUSTOMER SERVICE</h5><ul><li>Help &amp; Contact</li><li>Shipping &amp; Returns</li><li>Order Tracking</li><li>Size Guide</li><li>Gift Cards</li></ul></div>
    <div><h5>COMPANY</h5><ul><li>About Us</li><li>Blog</li><li>Venue Hire</li><li>Classes</li><li>Contact Us</li><li>Careers</li></ul></div>
    <div><h5>SOCIAL MEDIA</h5><ul><li>Photos</li><li>Friends</li><li>Updates</li><li>Events</li></ul></div>
    <div><h5>ARCHIVE</h5><ul><li>March 2024</li><li>April 2024</li><li>May 2024</li><li>June 2024</li><li>July 2024</li></ul></div>
  </div>
  <div class="payments"><span></span><span></span><span></span><span></span><span></span></div>
</footer>

</div>
</body>
</html>
```